My Professional Resume/CV Design

Hi Pixel Harbor experts, I need a professional resume/CV design for using my carrier hiring activities. I have a draft and this draft is 2 types.
1) Traditional IT Major Company Senior(Manager Level) to Director level application (File: Tanabe_Mirei_Res_EN2023AprA)
>Application example companies: Velmora, Drant, Quenta, Tidewicket, VossLattice, Brisk Vale, Hexaplume, Korvani, Zuvetra, Ferno, uMox, Wirlpeak etc
>This should not be fancy. Please make format with traditional/gentle/standard but also need to appear unique point such as icons, borderlines etc
2) Cutting-Edge (Web 3.0/metaverse/NFT/Crypto) Start-up or Young (Less 5 year's history) Company Director and C-Levels position application (Tanabe_Mirei_Res_EN2023Apr_typeC)
>Application Example Companies: Perilux Studios, Quorvex, Nexlorry.net, Dovecrest, FarDune, KelpVaultix, Ravello, Zipo/Tolk/Verm, Plunket, VESKARD, quillNRX etc
>This resume format should be something "edge" "advanced" "future" and "high-tech", so need to your high sense of design technics.
Both drafts is without a profile picture, but I need to put in my portfolio picture (Just attached one is my 2018's, you can trim and edit as well)
For the document format, please send me to WORD and PAGES both. and total MAX 2 page in all contents please (No more 3 pages)
Target Market(s)
Traditional Major Tech Company's VP/Directors or/and Latest Web 3.0 StartUp C-Levels (CEO/CTO/CSO/COO etc)
Industry/Entity Type
Technology
Font styles to use
Other font styles liked:
- Choose 3 a)Century Gothic b) Avenir c)Graphik d)Kohinoor e)Optima f)Platino
Look and feel
Each slider illustrates characteristics of the customer's brand and the style your logo design should communicate.

```html
<!DOCTYPE html>
<html lang="en">
<head>
<meta charset="utf-8">
<title>Mirei Tanabe — Resume</title>
<link href="https://fonts.googleapis.com/css2?family=Montserrat:wght@400;500;600;700&display=swap" rel="stylesheet">
<style>
:root{
  --bg:#e4e4e6;
  --paper:#ffffff;
  --plum:#a6499f;
  --blush:#e2b8de;
  --ink:#231f20;
  --text:#3a3a3a;
  --rule:#d9d9d9;
}
*{box-sizing:border-box;margin:0;padding:0}
html,body{width:1200px;height:591px;overflow:hidden;background:var(--bg);font-family:"Montserrat",sans-serif;color:var(--text)}
.canvas{position:relative;width:1200px;height:591px}
.page{position:absolute;top:54px;width:342px;height:483px;background:var(--paper);box-shadow:0 6px 10px -4px rgba(0,0,0,.25);overflow:hidden}
.page-1{left:57px}.page-2{left:429px}.page-3{left:802px}

/* headers */
.band{position:absolute;left:0;top:0;width:100%;background:var(--plum)}
.band-main{height:127px}
.band-small{height:47px}
.stripe{position:absolute;left:0;background:var(--blush)}
.portrait{position:absolute;border-radius:50%;background:#fff;display:flex;align-items:center;justify-content:center}
.portrait .photo{border-radius:50%;background:radial-gradient(circle at 50% 40%,#6b5a52 0%,#2b2421 55%,#151212 100%)}
.name{position:absolute;color:#fff;font-weight:700;letter-spacing:.3px;line-height:1;white-space:nowrap}
.place{position:absolute;color:#fff;font-weight:400;line-height:1;white-space:nowrap}
.page-1 .name{left:133px;top:16px;font-size:15.5px}
.page-1 .place{left:133px;top:33px;font-size:7px}
.page-2 .name,.page-3 .name{left:50px;top:13px;font-size:12.5px}
.page-2 .place,.page-3 .place{left:50px;top:29px;font-size:6px}

.side-head{position:absolute;left:133px;width:193px;color:#fff;font-weight:600;font-size:5.5px;border-bottom:.5px solid rgba(255,255,255,.7);padding-bottom:1px}
.side-text{position:absolute;left:133px;width:193px;color:#fff;font-size:3.3px;line-height:4.2px}
.path-row{display:flex;justify-content:space-between;color:#fff;font-size:3.1px;line-height:6px;white-space:nowrap}

/* role banner */
.role-back{position:absolute;left:12px;top:126px;width:318px;height:18px;border-radius:9px;background:var(--blush)}
.role{position:absolute;left:15px;top:124px;width:311px;height:22px;border-radius:11px;background:var(--ink);color:#fff;text-align:center;padding-top:4px;white-space:nowrap}
.role-title{font-size:6.2px;font-weight:500;letter-spacing:0;color:#f1dcef;line-height:7.5px}
.role-sub{font-size:3.9px;line-height:5px}

/* body text */
.para{position:absolute;left:20px;width:301px;font-size:4.4px;line-height:6.7px;text-align:justify;color:var(--text)}
.small{font-size:3.7px;line-height:6.6px;text-align:justify}
.section{position:absolute;left:19px;width:303px;font-size:7px;font-weight:500;color:var(--ink);border-bottom:.5px solid var(--rule);padding-bottom:3px;letter-spacing:.2px}
.bar{position:absolute;left:19px;width:303px;height:9.5px;border-radius:5px;display:flex;justify-content:space-between;align-items:center;padding:0 4px;font-size:3.9px;color:#fff;white-space:nowrap}
.bar.plum{background:var(--plum)}
.bar.ink{background:var(--ink)}
.bar.edu{font-size:4.6px}

.hl{position:absolute;left:19px;width:303px;font-size:3.9px;line-height:4.8px;color:var(--ink);padding:0 6px}
.hl.pill{background:var(--ink);color:#fff;border-radius:9px;display:flex;align-items:center}

ul.list{list-style:none}
ul.list li{position:relative;padding-left:4px}
ul.list li::before{content:"·";position:absolute;left:0}
.note{color:var(--ink);font-weight:500}

/* competencies */
.comp{position:absolute;top:290px;font-size:3.9px;line-height:6.6px;color:var(--ink);list-style:none}
.comp-rule{position:absolute;top:288px;width:.5px;height:42px;background:var(--rule)}

.foot{position:absolute;left:19px;top:464px;width:304px;height:11px;border-radius:6px;background:var(--ink);color:#fff;font-size:3.9px;letter-spacing:1.1px;display:flex;align-items:center;justify-content:center;white-space:nowrap;overflow:hidden}
.foot .sep{margin:0 7px}
</style>
</head>
<body>
<div class="canvas">

  <section class="page page-1">
    <div class="band band-main"></div>
    <div class="stripe" style="top:34px;width:30px;height:66px"></div>
    <div class="portrait" style="left:14px;top:12px;width:108px;height:108px">
      <div class="photo" role="img" aria-label="Portrait photo of Mirei Tanabe" style="width:97px;height:97px"></div>
    </div>
    <h1 class="name">MIREI TANABE</h1>
    <p class="place">(Wanchai, Hong Kong)</p>

    <h2 class="side-head" style="top:54px">PROFILE</h2>
    <p class="side-text" style="top:64px">Seniorbusiness Leader, Strategist And Driver Of Change. Worked In Over 30 Countries Across 4 Continents.passion For Company Turnaround, Business Development And Growth.</p>
    <h2 class="side-head" style="top:79px">CAREER PATH</h2>
    <div class="side-text" style="top:89px">
      <div class="path-row"><span>Inside Renewals Sales | Corvane Networks. | Hong Kong | Part Time</span><span>Jul 2022 - Present</span></div>
      <div class="path-row"><span>Guild Business Division Sales Operation Head | Lumenrail Works Japan | Hong Kong</span><span>Early 2022</span></div>
      <div class="path-row"><span>Business Development Manager | Orvic HK Limited | Hong Kong</span><span>Apr 2021- Apr 2022</span></div>
      <div class="path-row"><span>Business Development| Manager Teslin High-Tech (Hong Kong) Limited | Hong Kong</span><span>Aug 2020 – Apr 2021</span></div>
    </div>

    <div class="role-back"></div>
    <div class="role">
      <div class="role-title">BUSINESS DEVELOPMENT | VENDOR MANAGEMENT | PARTNER CHANNEL SALES</div>
      <div class="role-sub">Web 3+ Technology &amp; Cyber Security / Strategic Planning &amp; Execution / Proposal &amp; Contract Management</div>
    </div>

    <p class="para" style="top:151px">My value and career will only increase in a diverse and multinational work environment High-impact growth-oriented professional demonstrating a strong grasp of current marketing tools and strategies aligned with Cutting-edge technology with an interest in the transformation of society/era events within the industry and cyber security with an Entrepreneurial spirit. Strategically collaborate with external vendors and internal business partners; manages various commercial platforms, systems, domains, and channels to ensure scale marketing and lead development capabilities in line with business growth plans that deliver high-quality results. Participate in supply chain strategy development, developing implementation plans, and methods of dealing with business. Display strong analytical ability to evaluate end-to-end customer experience across multiple channels and customer touchpoints. Highly creative with experience in identifying target audiences and devising digital campaigns while valuing traditional methods that engage, inform, and motivate while staying abreast of industry trends. Conclude below 3 is my core abilities. “Cutting-Edge Technologies” “Business Development” and “Japan/APAC/Global Channel Sales”</p>

    <h2 class="section" style="top:226px">EDUCATION</h2>
    <div class="bar plum edu" style="top:241px"><span>Bachelor’s degree in economics/Philosophy</span><span>Eastbrook University, Japan</span></div>

    <h2 class="section" style="top:258px">HIGHLIGHTS OF QUALIFICATION</h2>
    <div class="hl pill" style="top:277px;height:17px">· Expert levels of sense of abilities in conducting marketing research and analyzing data strategically to identify brand/product value propositions, prospect customers, markets, and major competitors</div>
    <div class="hl" style="top:297px">· Understands target audiences and competition dynamics with insights from various sources while leading integrated digital and offline marketing campaigns from concept to execution, on time and within scope and budget.</div>
    <div class="hl pill" style="top:311px;height:17px">· Serve as supply chain interface for all major projects, with clear knowledge of project progress, logistics, and distribution development as well as implementation and execution of local and regional projects.</div>
    <div class="hl" style="top:332px">· Fluent in English and Japanese to communicate compelling value propositions for existing / prospective customers through different channels, digital/social communication, partnership, and sponsorship regularly and on a project basis.</div>
    <div class="hl pill" style="top:346px;height:17px">· Conceptualize and develop brand/product sales plans and campaigns for companies and individual business lines, including planning, liaison, coordination, and execution.</div>

    <h2 class="section" style="top:372px">PROFESSIONAL EXPERIENCE</h2>
    <div class="bar plum" style="top:385px"><span>Inside Renewals Sales | Corvane Networks. | Hong Kong | Part Time</span><span>Jul 2022 - Present</span></div>
    <p class="para small" style="top:396px">First visa-sponsored employee since the establishment of the APAC Hong Kong company (2017 and in total over 100+). Promotion to Territory Manager (Inside New Sales) is factored in. The agreement to start with renewal sales was to be able to build relationships with existing partners and to set the stage for the new position. Due to internal circumstances, there is no budgetary visibility for an Inside Sales Manager for the Japan Territory. Job hunting activity while still employed for reasons of wanting to advance own careers external, as prospects for promotion within the company are very low expectations by company reasons.</p>

    <footer class="foot">MIREI TANABE<span class="sep">|</span>MTANABE204@MAILBOX.EXAMPLE<span class="sep">|</span>+852 5550 0142/5550 0198</footer>
  </section>

  <section class="page page-2">
    <div class="band band-small"></div>
    <div class="stripe" style="top:11px;width:12px;height:25px"></div>
    <div class="portrait" style="left:6px;top:5px;width:38px;height:38px">
      <div class="photo" role="img" aria-label="Portrait photo of Mirei Tanabe" style="width:33px;height:33px"></div>
    </div>
    <h1 class="name">MIREI TANABE</h1>
    <p class="place">(Wanchai, Hong Kong)</p>

    <ul class="para small list" style="top:58px">
      <li>Distributor and Reseller (Partner) Management: Before I join, Corvane was the low position for any of the partner’s sales, like quotation production due to only focused PO. I focusing what end users face on the problems and pain and shared with proper partners. A result, they never ask me for a quotation (they now can quote themself) and they proposed me to new sales plans and strategies. I just concentrated to do what my partner want and relationship development.</li>
      <li>Co-work with Territory Regional Team remotely: Mainly Japan Sales, SEs, CS, Technical Support</li>
      <li>Enhancing mutual synergies with other regional teams: Corporate team works with especially APAC another region team ( India/SEA/ANZ/China total 4 regions) and US and EMEA as well.</li>
    </ul>

    <div class="bar plum" style="top:108px"><span>Guild Business Division Sales Operation Head | Lumenrail Works Japan | Hong Kong</span><span>Early 2022</span></div>
    <p class="para small" style="top:121px">This entity is an NFT GameFi startup for “Play To Earn” players scholarship program. I joined as the authorized person under CEO. My role is a huge territory, from community management to design strategy and tactics for this scholarship business.</p>

    <div class="bar ink" style="top:141px"><span>Business Development Manager | Orvic HK Limited | Hong Kong</span><span>Apr 2021- Apr 2022</span></div>
    <p class="para small" style="top:154px">Join from GM’s direct invitation due to he wanna survive the pandemic crisis, this is an IT reseller business provider in Hong Kong, China, SEA, and Japan market. Upon long-term mainly prospective business development and strategy, then proposed better to downsizing and restructuring, I suggest leaving this company and GM accepted (Still best relationships)</p>

    <div class="bar plum" style="top:181px"><span>Business Development| Manager Teslin High-Tech (Hong Kong) Limited | Hong Kong</span><span>Aug 2020 – Apr 2021</span></div>
    <p class="para small" style="top:194px">Start from BD of medical digital devices (Organic disinfection water, see HP: purenva.example) constructing frameworks for saving COVID-19 pandemic. After the project timeline and to-dos were fixed, received direct offer from president of next company to move on.</p>

    <div class="bar ink" style="top:214px"><span>Business Development Manager | Fenwick Global | Hong Kong</span><span>Apr2019 –Mar 2020</span></div>
    <p class="para small" style="top:227px">Demonstrate mastery in the production of a new TV program with Calderon National News Agency (TV station) for introducing cutting-edge science such as human-type robots; creating program/production budgets and completed all interactions with the research institute on behalf of the TV station and also planned the 12 episodes of the first episode</p>

    <div class="bar plum" style="top:254px"><span>Head of Division | Quarrow Tech Limited(Former Halvard Consulting, Company name changes) | Hong Kong</span><span>Sep 2018 – Mar 2019</span></div>
    <p class="para small" style="top:266px">Pioneered a zero-based customized Crypto Exchange platform, overseeing process improvement initiatives and facilitating prompt delivery to clients. Direct staff operations for the total IEO / STO business production, building and maintaining strategic relationships with all levels of stakeholders. Earned 3million HKS in 3 months of working on the BPO’s contract for the establishment of cryptocurrency exchange and new products (token), delivering the product by the deadline and succeeded in restructuring a negative company business into a profit-oriented enterprise. Stellar record of outperforming corporate expectations in meeting goals and objectives while strengthening effective communications with internal stakeholders, vendor and client team members.</p>
    <ul class="para small list" style="top:315px">
      <li>Participated in high-profile business trip meetings, managed and oversaw daily chat communications as well as prepared and presented operational reports to management and key stakeholders.</li>
      <li>Orchestrate the provision of outstanding oversight for five diverse internal departments and three regions (HK, Philippines and Japan) utilizing multipl business management software and remote work applications including video meetings.</li>
      <li>Exceeded expectations in creating and managing content for movies and documents including white paper writing, Community Management, increasing market positioning, and optimizing revenue growth.</li>
      <li>Appraised for developing and delivering tokens to clients using exceptional customer service management to generate business while facilitating customers’ integration wallet and listing exchange for a casino operator’s ICO project.</li>
      <li>Mastermind the process of instituting infrastructures and external vendor systems such as Customer Due Diligence, and trading systems to the ICO platform.</li>
      <li>Displayed solid leadership abilities in team building / mentoring activities and optimized project branding processes involving HR oversight and staffing as well as financial control for the ICO project.</li>
      <li>Recognized for extensive financial acumen and expertise in budget controls (P&amp;L, BS), generated a record $1.2 M in profit and achieved all ICO requirements while successfully listing one exchange at a time.</li>
      <li>Accomplished in diverse Ad-hoc operations encompassing accounting, payroll management, contract oversight, as well as corporate liaison with vendors, exchanges and other multi-functional professionals involved in project works.</li>
    </ul>
    <p class="para small note" style="top:425px">*As I could not expect any further promotion, I transfer to further develop my career and gain multi-national business acumen.</p>

    <footer class="foot">MIREI TANABE<span class="sep">|</span>MTANABE204@MAILBOX.EXAMPLE<span class="sep">|</span>+852 5550 0142/5550 0198</footer>
  </section>

  <section class="page page-3">
    <div class="band band-small"></div>
    <div class="stripe" style="top:11px;width:12px;height:25px"></div>
    <div class="portrait" style="left:6px;top:5px;width:38px;height:38px">
      <div class="photo" role="img" aria-label="Portrait photo of Mirei Tanabe" style="width:33px;height:33px"></div>
    </div>
    <h1 class="name">MIREI TANABE</h1>
    <p class="place">(Wanchai, Hong Kong)</p>

    <div class="bar ink" style="top:59px"><span>Senior Manager | Halvard Consulting International, Hong Kong</span><span>May 2016 –Sep 2018 (Mar 2019)</span></div>
    <p class="para small" style="top:71px">Outperformed corporate expectations in leading and supervising cryptocurrency white label exchange operations by improving systems that cannot be managed by email / chats, utilizing project management software, solving unexpected issues, and implementing process improvement initiatives and manuals. Adept in managing multiple projects, achieving stable operational exchange, and contributing to end user increase from 1500 to 5000. Reputed for consistent updates to the ever-changing customers’ desired requirements on the platform to achieve strategic goals. Named as Taiwan’s market project leader by the CEO, overseeing a remote team of professionals located in Tokyo, Osaka, Hong Kong, and Europe. Monitored specific project progress and status while also communicating and liaising between client and Fintech Service Vendors (B2B and B2C businesses) to build consensus</p>
    <ul class="para small list" style="top:121px">
      <li>Played a key role in leading and managing Customer Due Diligence (KYC/KYB) operations including the creation manual to manage risk and prevent financial misconduct for CS (Customer Success)</li>
      <li>Competently developed new tokens and adhered to clients’ requests in establishing an on-time implementation exchange platform to ease the process of exchanging major cryptocurrencies such as BTC/ETH/LTC.</li>
      <li>Promptly delivered exchange debit cards linked with the customers’ cryptocurrency wallet while crypto compliance changes.</li>
      <li>Spearheaded global business operations while overseeing the Taiwan subsidiary business expansion set up to encompass crypto-fiat trading, hiring and training staff, deposit/withdrawal operations to Taiwanese partner b2b clients, and bulk trading. Generated 500 initial customers before handover to the local manager.</li>
    </ul>
    <p class="para small note" style="top:175px">*Company name just changed from Halvard Consulting International Limited to Quarrow Tech Limited (Same Shareholders)</p>

    <div class="bar plum" style="top:188px"><span>Project Manager | PT. SERULA BALI | Denpasar</span><span>2014 – 2015</span></div>
    <ul class="para small list" style="top:201px"><li>Strategic planning of corporate projects with B2B institutions at Bali of Indonesia Microfinance and Property Corporate.</li></ul>
    <p class="para small note" style="top:209px">*Relocate to Hong Kong by personal reason at the time late 2015</p>

    <div class="bar ink" style="top:220px"><span>Chief Operation Officer | Merido Agency | Tokoyo</span><span>2010 – 2014</span></div>
    <ul class="para small list" style="top:233px"><li>Structured and pioneered the process of running the Tokyo branch of a Singaporean restaurant by connecting with the F&amp;B company. Demonstrated strength in PR including the English Media to increase brand awareness and clientele growth.</li></ul>
    <p class="para small note" style="top:249px">*The business cessation requirements of the JV Agreement are met. (Reason cannot be given due to confidentiality, but I can answer orally.)</p>

    <h2 class="section" style="top:271px">CORE COMPETENCIES</h2>
    <ul class="comp" style="left:19px">
      <li>· Global Operations Management</li><li>· Strategic Partnerships</li><li>· Process Improvement Champion</li><li>· Strategic Planning &amp; Execution</li><li>· Cryptocurrency | B2B B2B2C</li><li>· Research &amp; Development</li>
    </ul>
    <div class="comp-rule" style="left:116px"></div>
    <ul class="comp" style="left:139px">
      <li>· Key Account Management</li><li>· Business Restructuring</li><li>· Team Leadership / Management</li><li>· P &amp; L / Revenue Growth</li><li>· Budget Management</li><li>· Channel Sales B2B + B2C</li>
    </ul>
    <div class="comp-rule" style="left:233px"></div>
    <ul class="comp" style="left:256px">
      <li>· Staff Training / Retention</li><li>· Business Administration</li><li>· Supply Chain Management</li><li>· Vendor / Partner Management</li><li>· Negotiations &amp; Agreements</li><li>· Records &amp; Documentation</li>
    </ul>

    <footer class="foot">MIREI TANABE<span class="sep">|</span>MTANABE204@MAILBOX.EXAMPLE<span class="sep">|</span>+852 5550 0142/5550 0198</footer>
  </section>

</div>
</body>
</html>
```